Need Beautiful Banners for On-Site Marketing

Hello,
We are looking to create some banners for use on our site to highlight some features of our business. Our inspiration for these banners and their placement comes from the design on http://www.buyvane.com. We like their marketing banners and would like to create something along these lines.
I've uploaded two files to show exactly how and where these banners will be fitting into our design. **Disregard the Blue color used in the example files** Also, the larger banner ad in the uploaded files is incorrect height. Refer below for sizes.
There are two sizes for the banners:
1. Small - 475px Width and Approx. 45px Height. Seen under the header on our site.
2. Large - 960px Width and Approx. 45px height. These will be used in the content portions of the site and spread across width of page.
5 Banners needed with the following details:
1. (Small) - First Time Buyer Discount - 5% - Use checkout code "First5".
This banner will not be a link, so no need for a button or arrow signifying link.
2. (Small). Larger Orders? No problem! Save Time and Money Today. Get a Quote Now.
This banner will be linked to a quote page.
3. (Large) We are Stoutware Commercial Specialist! - Expert Service, Lower Pricing, Larger Catalog, More Replacement Parts.
This banner will be linked to our "about-us" page.
4. (Large) $65 million+ Inventory Across 31 Distribution Centers. Larger Catalog, Lower Prices, Fast 1-2 Day Shipping.
This banner will be linked to our shipping page.
5. (Large) Introducing our State-of-the-Art Inventory Tool:
Check Live local stock levels at 31 Nationwide Distribution Centers Today!
This will be linked to an informational page.
So.. 2 Small and 3 Large Banners. All text in these banners can be edited how you see fit. We'd like to have at least some continuity across the designs for all banners. If you look at buyvane.com, they use the same skinny text and link button graphics in most of their banners.
Thanks!! Looking forward to these designs!
Reason: Really need something more for 5 banners.. Anyone?

```html
<!DOCTYPE html>
<html lang="en">
<head>
<meta charset="utf-8">
<title>First Time Buyer Discount Banner</title>
<link href="https://fonts.googleapis.com/css2?family=Arimo:wght@700&display=swap" rel="stylesheet">
<style>
  :root {
    --page-bg: #ffffff;
    --red-top: #f2141c;
    --red-mid: #d80008;
    --red-low: #b00006;
    --red-base: #8a0004;
    --text-light: #ffffff;
    --outline-dark: #6e0003;
  }
  html, body {
    margin: 0;
    padding: 0;
    width: 1200px;
    height: 888px;
    overflow: hidden;
    background: var(--page-bg);
  }
  .canvas {
    position: relative;
    width: 1200px;
    height: 888px;
  }
  .promo-banner {
    position: absolute;
    left: 29px;
    top: 389px;
    width: 1140px;
    height: 108px;
    border-radius: 12px;
    background: linear-gradient(to bottom,
      var(--red-top) 0%,
      var(--red-mid) 45%,
      var(--red-low) 80%,
      var(--red-base) 100%);
    font-family: "Arimo", Arial, sans-serif;
    font-weight: 700;
    color: var(--text-light);
    overflow: hidden;
  }
  .promo-banner::before {
    content: "";
    position: absolute;
    left: 0; right: 0; top: 0;
    height: 48%;
    background: linear-gradient(to bottom, rgba(255,255,255,0.18), rgba(255,255,255,0.04));
  }
  .audience {
    position: absolute;
    left: 24px;
    top: 55px;
    transform: translateY(-50%);
    font-size: 36px;
    letter-spacing: -0.3px;
    text-shadow: 0 2px 2px rgba(80,0,0,0.6);
  }
  .chevron {
    position: absolute;
    left: 355px;
    top: 41px;
    width: 26px;
    height: 30px;
  }
  .offer {
    position: absolute;
    left: 403px;
    top: 55px;
    transform: translateY(-50%);
    font-size: 50px;
    letter-spacing: -1px;
    -webkit-text-stroke: 6px var(--outline-dark);
    paint-order: stroke fill;
    text-shadow: 0 3px 3px rgba(60,0,0,0.7);
  }
  .code-block {
    position: absolute;
    left: 795px;
    width: 320px;
    top: 0;
    height: 108px;
    text-align: center;
    text-shadow: 0 2px 2px rgba(80,0,0,0.6);
  }
  .code-label {
    position: absolute;
    left: 0; right: 0;
    top: 10px;
    font-size: 32px;
  }
  .code-value {
    position: absolute;
    left: 0; right: 0;
    top: 56px;
    font-size: 40px;
  }
</style>
</head>
<body>
<div class="canvas">
  <div class="promo-banner">
    <span class="audience">First Time Buyer</span>
    <svg class="chevron" viewBox="0 0 26 30" aria-hidden="true">
      <path d="M4 3 L20 15 L4 27 L2 21 L12 15 L2 9 Z" fill="#ffffff"/>
    </svg>
    <span class="offer">Discount - 5%</span>
    <div class="code-block">
      <span class="code-label">Use checkout code</span>
      <span class="code-value">“First5”</span>
    </div>
  </div>
</div>
</body>
</html>
```